New website

Our website (www.larchhollow.com) needs to be replaced with something gorgeous and glossy. We do like the text of our current website but have many new images to put on the site. We want to create a website that shows viewers what our team can do, and how we can create something amazing for them and their homes.

Coding

```html
<!DOCTYPE html>
<html lang="en">
<head>
<meta charset="utf-8">
<title>Larch Hollow Landscaping</title>
<link href="https://fonts.googleapis.com/css2?family=Alegreya+SC:wght@500;700&family=Roboto:wght@300;400;500;700&family=Montserrat:wght@700;800&display=swap" rel="stylesheet">
<style>
:root{
  --green:#4cb75b;
  --green-dark:#3ea34d;
  --blue:#2f86cf;
  --ink:#1c1c1c;
  --text:#5b5b5b;
  --grey-bg:#f6f6f6;
  --footer:#1b1b1b;
  --white:#ffffff;
}
*{box-sizing:border-box;margin:0;padding:0}
html,body{width:1200px;height:4648px;overflow:hidden}
body{position:relative;background:var(--white);font-family:"Roboto",Arial,sans-serif;color:var(--text)}
.abs{position:absolute}
.btn{position:absolute;display:flex;align-items:center;justify-content:center;background:var(--green);color:var(--white);border-radius:30px;font-family:"Montserrat",Arial,sans-serif;font-weight:800;font-size:13px;letter-spacing:1.5px;text-transform:uppercase}
.eyebrow{position:absolute;left:0;width:100%;text-align:center;color:var(--green);font-size:15px}
.section-title{position:absolute;left:0;width:100%;text-align:center;font-family:"Alegreya SC",Georgia,serif;font-weight:500;font-size:44px;color:var(--ink);letter-spacing:1px}
.photo{position:absolute}

/* header */
.topbar{top:0;left:0;width:1200px;height:87px;background:var(--white)}
.logo{position:absolute;font-family:"Alegreya SC",Georgia,serif;font-weight:500;letter-spacing:5px;color:#4a4a4a;white-space:nowrap}
.top-info{position:absolute;display:flex;align-items:center;gap:14px}
.top-info .ico{width:44px;height:44px;border-radius:50%;background:var(--green);display:flex;align-items:center;justify-content:center}
.top-info b{display:block;font-size:13px;color:var(--ink);font-weight:700}
.top-info span{display:block;font-size:15px;color:#555;margin-top:3px}
.nav{top:87px;left:0;width:1200px;height:58px;background:var(--blue)}
.nav ul{list-style:none;display:flex;position:absolute;left:105px;top:0;height:58px;align-items:center;gap:48px}
.nav li{color:var(--white);font-size:16px;text-transform:uppercase}
.nav li.active{font-weight:700}
.schedule{position:absolute;z-index:10;left:861px;top:81px;width:339px;height:92px;background:var(--green);border-radius:0 0 0 30px}
.schedule .ring{position:absolute;left:1px;top:2px;width:64px;height:64px;border-radius:50%;background:var(--green);border:3px solid var(--white);display:flex;align-items:center;justify-content:center}
.schedule small{position:absolute;left:80px;top:22px;color:var(--white);font-family:"Montserrat",Arial,sans-serif;font-weight:700;font-size:13px;letter-spacing:.5px;white-space:nowrap}
.schedule strong{position:absolute;left:79px;top:40px;color:var(--white);font-family:"Montserrat",Arial,sans-serif;font-weight:800;font-size:28px;line-height:36px;letter-spacing:.5px;white-space:nowrap}

/* hero */
.hero{top:145px;left:0;width:1200px;height:568px;overflow:hidden}
.hero .photo{inset:0;background:linear-gradient(120deg,#2d3a2a 0%,#4e5a48 35%,#6d7466 55%,#5b6b45 78%,#3b5a2c 100%)}
.hero .shade{position:absolute;inset:0;background:linear-gradient(90deg,rgba(0,0,0,.45),rgba(0,0,0,.05) 70%)}
.hero-welcome{position:absolute;left:105px;top:128px;color:var(--white);font-family:"Alegreya SC",Georgia,serif;font-size:24px;letter-spacing:11px}
.hero-title{position:absolute;left:103px;top:172px;color:var(--white);font-family:"Alegreya SC",Georgia,serif;font-weight:500;font-size:68px;letter-spacing:8px;line-height:1;white-space:nowrap}
.hero-sub{position:absolute;left:105px;top:253px;color:var(--white);font-family:"Alegreya SC",Georgia,serif;font-size:38px;letter-spacing:13px}
.hero-wave{position:absolute;left:0;bottom:0;width:1200px;height:140px}

/* services */
.card{position:absolute;top:917px;width:307px;height:364px;background:var(--white);border-radius:0 0 40px 0;box-shadow:0 6px 14px rgba(0,0,0,.12);overflow:hidden}
.card .photo{left:0;top:0;width:100%;height:189px}
.card h3{position:absolute;top:222px;width:100%;text-align:center;font-size:17px;font-weight:500;color:var(--ink);letter-spacing:.5px}
.card p{position:absolute;top:257px;left:18px;right:18px;text-align:center;font-size:14.5px;line-height:23px;color:#6a6a6a}
.card svg{position:absolute;top:306px;left:141px}
.slider-arrow{position:absolute;top:1057px;width:40px;height:40px;border-radius:50%;display:flex;align-items:center;justify-content:center}

/* about */
.about{top:1465px;left:0;width:1200px;height:610px;background:var(--grey-bg)}
.about .kicker{position:absolute;left:105px;top:67px;color:var(--green);font-size:15px}
.big-title{position:absolute;font-family:"Alegreya SC",Georgia,serif;font-weight:500;font-size:42px;line-height:45px;color:var(--ink);letter-spacing:.5px}
.body-copy{position:absolute;font-size:15px;line-height:25px;color:#666}

/* stats */
.stats{top:2075px;left:0;width:1200px;height:231px;background:linear-gradient(90deg,#4db35a,#56bd63 50%,#4bb158)}
.stat{position:absolute;top:60px;width:200px;text-align:center;color:var(--white)}
.stat b{display:block;font-weight:400;font-size:80px;line-height:80px;letter-spacing:2px}
.stat span{display:block;font-size:14px;margin-top:12px;letter-spacing:.5px}

/* testimonials */
.reviews{top:2907px;left:0;width:1200px;height:437px;background:linear-gradient(180deg,#52b85f,#4aae56)}
.reviews .eyebrow{color:var(--white);top:56px}
.reviews .section-title{color:var(--white);top:88px}
.avatar{position:absolute;border-radius:50%;border:3px solid var(--white)}
.quote{position:absolute;left:270px;width:660px;top:258px;text-align:center;color:var(--white);font-style:italic;font-weight:300;font-size:15.5px;line-height:23px}
.reviewer{position:absolute;top:314px;left:0;width:100%;text-align:center;color:var(--white);font-size:21px;font-weight:500}
.dots{position:absolute;top:352px;left:574px;display:flex;gap:12px}
.dots i{width:8px;height:8px;background:#1d1d1d}
.dots i.on{width:12px;height:12px;margin-top:-2px;background:var(--white)}

/* portfolio */
.tile{position:absolute}
.tile-overlay{position:absolute;inset:0;background:rgba(20,20,20,.55)}

/* footer */
.footer{top:4150px;left:0;width:1200px;height:498px}
.footer-bg{position:absolute;left:0;top:0;width:1200px;height:498px}
.footer h4{position:absolute;top:166px;color:var(--white);font-family:"Alegreya SC",Georgia,serif;font-weight:500;font-size:26px;letter-spacing:.5px}
.footer ul{position:absolute;list-style:none;top:210px}
.footer li{color:#e6e6e6;font-size:15px;line-height:35px;text-transform:uppercase}
.social{position:absolute;top:4448px;width:60px;height:60px;border-radius:50%;border:1.5px solid #e6e6e6}
.copyright{position:absolute;left:0;top:4607px;width:100%;text-align:center;color:#dcdcdc;font-size:13px}
</style>
</head>
<body>

<header class="abs topbar">
  <div class="logo" style="left:105px;top:28px;font-size:30px">LARCH HOLLOW</div>
  <div class="top-info" style="left:424px;top:21px">
    <div class="ico"><svg width="20" height="20" viewBox="0 0 24 24"><path fill="#fff" d="M6.6 10.8a15.1 15.1 0 0 0 6.6 6.6l2.2-2.2a1 1 0 0 1 1-.25 11.4 11.4 0 0 0 3.6.57 1 1 0 0 1 1 1V20a1 1 0 0 1-1 1A17 17 0 0 1 3 4a1 1 0 0 1 1-1h3.5a1 1 0 0 1 1 1c0 1.250.2 2.450.57 3.6a1 1 0 0 1-.25 1z"/></svg></div>
    <div><b>PHONE NO :</b><span>(555) 014-7720</span></div>
  </div>
  <div class="top-info" style="left:660px;top:21px">
    <div class="ico"><svg width="22" height="22" viewBox="0 0 24 24"><circle cx="12" cy="12" r="9" fill="none" stroke="#fff" stroke-width="2"/><path d="M12 7v5l3 2" fill="none" stroke="#fff" stroke-width="2" stroke-linecap="round"/></svg></div>
    <div><b>BUSINESS HOURS :</b><span>Monday-Saturday: 7:00am -7:00pm Closed Sunday</span></div>
  </div>
</header>

<nav class="abs nav">
  <ul>
    <li class="active">Home</li><li>About Us</li><li>Services</li><li>Testimonials</li><li>Blog</li><li>Contact Us</li>
  </ul>
</nav>

<section class="abs hero">
  <div class="photo" role="img" aria-label="Landscaper laying fresh turf beside a cobblestone path"></div>
  <div class="shade"></div>
  <div class="hero-welcome">WELCOME TO</div>
  <div class="hero-title">LARCH HOLLOW</div>
  <div class="hero-sub">LANDSCAPING</div>
  <div class="btn" style="left:105px;top:328px;width:180px;height:54px;font-size:12px">Make a Payment</div>
  <svg class="hero-wave" viewBox="0 0 1200 140" preserveAspectRatio="none">
    <path d="M0 40 C 220 130 520 150 820 95 C 990 62 1110 50 1200 62 L1200 140 L0 140 Z" fill="#fff"/>
    <path d="M40 60 C 260 125 540 140 820 92 C 990 62 1110 48 1200 58 L1200 70 C 1110 62 990 74 820 104 C 560 150 260 132 40 60 Z" fill="#2f86cf"/>
  </svg>
</section>

<div class="schedule">
  <div class="ring"><svg width="28" height="28" viewBox="0 0 24 24"><path fill="#fff" d="M6.6 10.8a15.1 15.1 0 0 0 6.6 6.6l2.2-2.2a1 1 0 0 1 1-.25 11.4 11.4 0 0 0 3.6.57 1 1 0 0 1 1 1V20a1 1 0 0 1-1 1A17 17 0 0 1 3 4a1 1 0 0 1 1-1h3.5a1 1 0 0 1 1 1c0 1.250.2 2.450.57 3.6a1 1 0 0 1-.25 1z"/></svg></div>
  <small>SCHEDULE AN APPOINTMENT</small>
  <strong>(555) 014-7720</strong>
</div>

<div class="eyebrow" style="top:803px">What We Do</div>
<h2 class="section-title" style="top:823px">Our Services</h2>

<div class="slider-arrow" style="left:34px;background:#1d1d1d"><svg width="12" height="12" viewBox="0 0 12 12"><path d="M8 2 4 6l4 4" fill="none" stroke="#fff" stroke-width="2"/></svg></div>
<div class="slider-arrow" style="left:1121px;background:var(--green)"><svg width="12" height="12" viewBox="0 0 12 12"><path d="M4 2l4 4-4 4" fill="none" stroke="#fff" stroke-width="2"/></svg></div>

<article class="card" style="left:105px">
  <div class="photo" role="img" aria-label="Lawn mower cutting bright green grass" style="background:linear-gradient(135deg,#3a3a3a 0%,#5a7d2c 45%,#6fb33a 100%)"></div>
  <h3>LAWN MAINTENANCE</h3>
  <p>Why should you have to spend hours on lawn maintenance just</p>
  <svg width="24" height="14" viewBox="0 0 24 14"><path d="M1 7h21M16 1l6 6-6 6" fill="none" stroke="#1d1d1d" stroke-width="2"/></svg>
</article>
<article class="card" style="left:446px">
  <div class="photo" role="img" aria-label="Gardener pruning a shrub with red secateurs" style="background:linear-gradient(135deg,#5aa53a 0%,#7cc050 50%,#4f9a2f 100%)"></div>
  <h3>LANDSCAPE MAINTENANCE</h3>
  <p>Larch Hollow provides landscaping and garden maintenance services</p>
  <svg width="24" height="14" viewBox="0 0 24 14"><path d="M1 7h21M16 1l6 6-6 6" fill="none" stroke="#1d1d1d" stroke-width="2"/></svg>
</article>
<article class="card" style="left:789px">
  <div class="photo" role="img" aria-label="Hands laying a roll of fresh sod" style="background:linear-gradient(160deg,#7a8a6a 0%,#6aa048 45%,#8ab46a 100%)"></div>
  <h3>LANDSCAPING</h3>
  <p>We can even show you how proper landscaping can improve your</p>
  <svg width="24" height="14" viewBox="0 0 24 14"><path d="M1 7h21M16 1l6 6-6 6" fill="none" stroke="#1d1d1d" stroke-width="2"/></svg>
</article>

<div class="btn" style="left:491px;top:1319px;width:218px;height:54px">View More Services</div>

<section class="abs about">
  <div class="kicker">About Us</div>
  <h2 class="big-title" style="left:105px;top:95px">TOP RATED GARDEN<br>&amp; LANDSCAPING<br>COMPANY</h2>
  <div class="body-copy" style="left:105px;top:250px;width:440px">
    <p>Established in 2005 as a way to pay for college tuition, Larch Hollow has instead become our passion. With a garage sale mower and a commitment to doing every job well, our list of satisfied customers grew quickly over the years.</p>
    <p style="margin-top:8px">While the scope of our landscaping company has grown, our way of doing business has not.</p>
  </div>
  <div class="btn" style="left:105px;top:424px;width:140px;height:54px">Read More</div>
  <div class="photo" role="img" aria-label="Gardener holding a potted pine seedling" style="left:590px;top:75px;width:246px;height:443px;background:linear-gradient(170deg,#1f8a5a 0%,#3b9a62 40%,#4f7a3a 70%,#2c2c2c 100%)"></div>
  <div class="photo" role="img" aria-label="Pruning shears cutting a dry branch" style="left:850px;top:143px;width:245px;height:375px;background:linear-gradient(160deg,#c89a6a 0%,#a87448 45%,#6a4a30 80%,#2aa6a0 100%)"></div>
</section>

<section class="abs stats">
  <div class="stat" style="left:144px"><b>42</b><span>LANDSCAPERS</span></div>
  <div class="stat" style="left:380px"><b>75</b><span>CLIENTS</span></div>
  <div class="stat" style="left:611px"><b>45</b><span>EQUIPMENTS</span></div>
  <div class="stat" style="left:847px"><b>20</b><span>EXPERIENCES</span></div>
</section>

<div class="photo" role="img" aria-label="Two-storey house with a manicured front lawn and flower beds" style="left:106px;top:2396px;width:475px;height:419px;border-radius:50px 0 90px 0;background:linear-gradient(180deg,#9cc3e6 0%,#c9d6de 30%,#a9a69a 48%,#5f8f3a 62%,#6fb03d 100%)"></div>
<div class="abs" style="left:641px;top:2395px;color:var(--green);font-size:15px">Why Choose Us</div>
<h2 class="big-title" style="left:641px;top:2425px">BOTH THE HEART AND<br>THE GARDEN MAY<br>BLOOM WITH BEAUTY</h2>
<p class="body-copy" style="left:641px;top:2578px;width:462px">You shouldn't have to spend hours on grounds maintenance to enjoy a well-designed and well-maintained yard. The landscaping professionals at Larch Hollow can handle your landscape maintenance, so you can focus on the demands of your family, job, and more.</p>
<div class="btn" style="left:641px;top:2716px;width:140px;height:54px">Read More</div>

<section class="abs reviews">
  <div class="eyebrow">Our Reviews</div>
  <h2 class="section-title">Client Testimonials</h2>
  <div class="avatar" role="img" aria-label="Client portrait" style="left:462px;top:172px;width:48px;height:48px;background:#c9a58a"></div>
  <div class="avatar" role="img" aria-label="Client portrait" style="left:512px;top:170px;width:52px;height:52px;background:#9a7a62"></div>
  <div class="avatar" role="img" aria-label="Client portrait" style="left:562px;top:158px;width:76px;height:76px;background:#b58e70"></div>
  <div class="avatar" role="img" aria-label="Client portrait" style="left:632px;top:170px;width:52px;height:52px;background:#8a8a92"></div>
  <div class="avatar" role="img" aria-label="Client portrait" style="left:676px;top:172px;width:48px;height:48px;background:#6a9ac0"></div>
  <p class="quote">Lorem ipsum dolor sit amet, onsecteturadipiscing elit, sed do eiusmod tempor incididunt ut labore et dolore naaliqua. Quis ipsum suspendisse ultrices gravida</p>
  <div class="reviewer">-Maren Tolliver</div>
  <div class="dots"><i></i><i class="on"></i><i></i></div>
</section>

<div class="eyebrow" style="top:3430px">Our Gallery</div>
<h2 class="section-title" style="top:3450px">Our Portfolio</h2>

<div class="tile" role="img" aria-label="Landscaped home front at dusk" style="left:105px;top:3546px;width:325px;height:274px;background:linear-gradient(180deg,#2a3340,#3c4a3a 60%,#4a6a3a)">
  <div class="tile-overlay"></div>
  <div class="logo" style="left:0;width:325px;text-align:center;top:100px;font-size:26px;color:#fff">LARCH HOLLOW</div>
  <div class="btn" style="left:91px;top:162px;width:142px;height:52px;font-size:12px">View Details</div>
</div>
<div class="tile" role="img" aria-label="Pickup truck with a snow plough in winter" style="left:105px;top:3829px;width:325px;height:180px;background:linear-gradient(180deg,#e6e8ea,#c9cdd0 60%,#9aa0a4)"></div>
<div class="tile" role="img" aria-label="Worker installing turf along a paver edge" style="left:438px;top:3546px;width:325px;height:180px;background:linear-gradient(160deg,#7a7a70,#6a9a48 55%,#4a7a30)"></div>
<div class="tile" role="img" aria-label="Trowel planting a seedling in soil" style="left:438px;top:3733px;width:325px;height:276px;background:linear-gradient(170deg,#9ac070,#5a9a38 50%,#3a6a28)"></div>
<div class="tile" role="img" aria-label="Stone house with fresh lawn and shrubs" style="left:771px;top:3546px;width:325px;height:274px;background:linear-gradient(180deg,#c8c0b0,#9a9080 40%,#6aa83a 60%,#5a9a30)"></div>
<div class="tile" role="img" aria-label="Garden with a curved stone path and trees" style="left:771px;top:3829px;width:325px;height:180px;background:linear-gradient(160deg,#2e5a22,#4a8a30 50%,#7ab848)"></div>

<div class="btn" style="left:530px;top:4034px;width:141px;height:55px">View More</div>

<footer class="abs footer">
  <svg class="footer-bg" viewBox="0 0 1200 498" preserveAspectRatio="none">
    <path d="M0 72 C 260 10 620 0 900 18 C 1040 28 1140 18 1200 6 L1200 498 L0 498 Z" fill="#1b1b1b"/>
    <path d="M0 66 C 260 2 620 -10 900 10 C 1040 20 1140 10 1200 0 L1200 12 C 1140 26 1040 34 900 24 C 620 6 260 16 0 76 Z" fill="#2f86cf"/>
  </svg>
  <div class="logo" style="left:105px;top:218px;font-size:40px;color:#8a8a8a;letter-spacing:9px">LARCH HOLLOW</div>
  <h4 style="left:615px">Quick Links</h4>
  <ul style="left:615px"><li>Home</li><li>About Us</li><li>Services</li><li>Testimonials</li><li>Blog</li><li>Contact Us</li></ul>
  <h4 style="left:837px">Our Services</h4>
  <ul style="left:837px;width:230px"><li>Lawn Maintenance</li><li style="line-height:25px;padding:5px 0">Irrigation Installation &amp; Maintenance</li><li>Landscape Maintenance</li><li>Landscaping</li><li>Lawn Core Aeration</li><li>More...</li></ul>
  <div class="abs" style="left:105px;top:434px;width:953px;height:1px;background:#3a3a3a"></div>
</footer>
<div class="social" role="img" aria-label="Social profile" style="left:212px"></div>
<div class="social" role="img" aria-label="Social profile" style="left:288px"></div>
<div class="social" role="img" aria-label="Social profile" style="left:363px"></div>
<div class="copyright">Copyright © 2025 Larch Hollow Landscaping . All Rights Reserved / Privacy and security</div>

</body>
</html>
```